TRV 25 year Anniversary - create file

I need an electronic Image file that I can incorporate into everything we are dong -including our pamphlets and brochures which we print in-house with Word Or Publisher files

The Plan mentor 25 file attached is the look we're after for part of our 25 year branding. I've included three of our different operating brands that should be incorporated into the letters. Other facts that can be included are :
123 combined years of experience
11792 Clients on file
11 Team Members
60% have been with us 5+ years
Service Entire Niagara Region
Carpet Cleaning
Oriental Rug Cleaning
Rug Binding
Making Custom Rugs
Winner of 8 Franchise Awards
Winner - Chamber of Commerce - "Excellence in Business"
Winner - Falcon Outreach's "Lift your Game " Award
Gwendolyn and Ray featured in magazine article "Partners in Commerce"
Supporters of the "Kids" programs at the QBFL
Supporters of our Local Health System

Colors
0255a3

Requirements
Must have
• final file must be a format that I can use to insert into other publications in Word and Publisher

```html
<!DOCTYPE html>
<html lang="en">
<head>
<meta charset="utf-8">
<title>TRV 25 Year Anniversary</title>
<link href="https://fonts.googleapis.com/css2?family=Source+Sans+3:wght@400;600;700;800&display=swap" rel="stylesheet">
<style>
  :root {
    --stage: #262626;
    --panel-light: #1f7cc6;
    --panel-dark: #0a55a3;
    --numeral-fill: #ffffff;
    --numeral-edge: #1b3f7a;
    --ink: #1b57a6;
    --ink-strong: #0f4c9a;
    --icon: #6d6e71;
  }
  * { margin: 0; padding: 0; box-sizing: border-box; }
  html, body { width: 1200px; height: 1000px; overflow: hidden; background: var(--stage); }
  body { font-family: "Source Sans 3", "Myriad Pro", sans-serif; color: var(--ink); }
  .canvas { position: relative; width: 1200px; height: 1000px; }
  .anniversary-panel {
    position: absolute; left: 83px; top: 104px; width: 1034px; height: 771px;
    background: radial-gradient(ellipse at 50% 50%, var(--panel-light) 0%, var(--panel-dark) 75%);
  }
  .numerals { position: absolute; left: 0; top: 0; width: 1200px; height: 1000px; }
  .numeral { fill: var(--numeral-fill); stroke: var(--numeral-edge); stroke-width: 1.5; }
  .icon { fill: var(--icon); }
  .fact { position: absolute; text-align: center; line-height: 1.15; }
  .big { font-weight: 700; color: var(--ink-strong); }
  .label { font-size: 16px; font-weight: 400; }
  .brand { position: absolute; font-weight: 800; color: var(--ink-strong); line-height: 1.05; }
</style>
</head>
<body>
<div class="canvas">
  <div class="anniversary-panel"></div>

  <svg class="numerals" viewBox="0 0 1200 1000" aria-hidden="true">
    <defs>
      <g id="person"><circle cx="0" cy="0" r="7"/><path d="M-11,28 v-12 c0,-6 5,-10 11,-10 c6,0 11,4 11,10 v12 z"/></g>
    </defs>

    <!-- numeral two -->
    <path class="numeral" d="M183,350 C183,230 290,155 395,155 C510,155 595,235 595,330 C595,420 540,480 460,560 L330,668 L595,668 L595,775 L170,775 L170,730 C175,690 200,650 240,612 L390,470 C440,420 470,390 470,340 C470,280 430,240 395,240 C350,240 310,280 310,350 Z"/>
    <!-- numeral five -->
    <path class="numeral" d="M710,155 L1060,155 L1060,260 L812,260 L806,370 C850,352 880,350 910,350 C1010,350 1090,450 1090,575 C1090,700 1000,778 880,778 C770,778 690,710 660,590 L790,590 C805,635 840,665 880,665 C940,665 975,620 975,560 C975,500 930,470 885,470 C840,470 810,490 800,500 L685,500 Z"/>

    <!-- handshake -->
    <path class="icon" d="M226,252 l18,-12 l14,6 l12,-6 l26,16 l-4,6 l-10,-6 l-8,6 l6,8 l-10,8 l-8,-6 l-6,6 l-10,-6 l-6,4 z"/>
    <!-- trophy -->
    <g class="icon">
      <path d="M487,210 h38 v18 c0,14 -8,24 -19,26 c-11,-2 -19,-12 -19,-26 z"/>
      <path d="M487,214 h-10 c0,12 6,18 12,20 v-5 c-4,-2 -6,-6 -6,-10 h4 z M525,214 h10 c0,12 -6,18 -12,20 v-5 c4,-2 6,-6 6,-10 h-4 z"/>
      <rect x="502" y="254" width="8" height="10"/>
      <rect x="490" y="264" width="32" height="10"/>
      <polygon points="507,182 510,190 518,190 512,195 514,203 507,198 500,203 502,195 496,190 504,190"/>
      <polygon points="472,228 474,234 480,234 475,237 477,243 472,239 467,243 469,237 464,234 470,234"/>
      <polygon points="536,228 538,234 544,234 539,237 541,243 536,239 531,243 533,237 528,234 534,234"/>
    </g>
    <!-- team pictograms -->
    <g class="icon">
      <use href="#person" x="432" y="455"/><use href="#person" x="470" y="455"/><use href="#person" x="508" y="455"/>
      <use href="#person" x="395" y="500"/><use href="#person" x="433" y="500"/><use href="#person" x="471" y="500"/>
      <use href="#person" x="335" y="545"/><use href="#person" x="373" y="545"/><use href="#person" x="411" y="545"/>
      <use href="#person" x="312" y="585"/><use href="#person" x="350" y="585"/>
    </g>
    <!-- thumbs up -->
    <path class="icon" d="M238,712 h8 v20 h-8 z M249,712 l8,-10 c2,-4 2,-8 6,-8 c4,0 4,6 2,12 h8 c4,0 5,4 3,6 c2,2 1,5 -1,6 c2,2 0,5 -2,6 c1,2 -1,4 -3,4 h-21 z"/>
    <!-- kids pictograms -->
    <g class="icon">
      <circle cx="530" cy="716" r="8"/><path d="M518,728 h24 v18 h-4 v24 h-6 v-20 h-4 v20 h-6 v-24 h-4 z"/>
      <circle cx="566" cy="716" r="8"/><path d="M558,728 h16 l8,22 h-6 v20 h-6 v-16 h-4 v16 h-6 v-20 h-6 z"/>
    </g>
    <!-- first place medallion -->
    <g>
      <path d="M722,205 c-6,-18 0,-34 12,-42 M790,205 c6,-18 0,-34 -12,-42" fill="none" stroke="#6d6e71" stroke-width="6"/>
      <circle class="icon" cx="756" cy="200" r="22"/>
      <text x="756" y="210" text-anchor="middle" font-family="Source Sans 3, sans-serif" font-weight="700" font-size="28" fill="#fff">1</text>
    </g>
    <!-- rolled rug -->
    <g class="rug-roll">
      <polygon class="icon" points="832,418 898,418 916,442 840,442"/>
      <path class="icon" d="M838,382 h40 a8,26 0 0 1 0,52 h-40 z"/>
      <circle class="icon" cx="838" cy="408" r="26"/>
      <path d="M838,408 a3,3 0 1 1 5,2 a8,8 0 1 1 -12,-7 a13,13 0 1 1 20,13 a18,18 0 1 1 -26,-20" fill="none" stroke="#fff" stroke-width="3"/>
    </g>
    <!-- award rosette -->
    <g class="icon">
      <polygon points="998,640 992,678 1004,670 1012,680 1016,648"/>
      <polygon points="1028,640 1034,678 1022,670 1014,680 1010,648"/>
      <circle cx="1013" cy="630" r="20"/>
      <circle cx="1013" cy="630" r="14" fill="#fff"/>
      <text x="1013" y="637" text-anchor="middle" font-family="Source Sans 3, sans-serif" font-weight="700" font-size="18" fill="#6d6e71">1</text>
    </g>
  </svg>

  <!-- numeral two content -->
  <div class="brand" style="left:312px; top:186px; font-size:17px; width:170px;">Tri-Valley<br>Carpet Works</div>

  <div class="fact" style="left:188px; top:285px; width:120px;">
    <div class="big" style="font-size:36px; line-height:1;">11792</div>
    <div class="label">Clients on file</div>
  </div>

  <div class="fact" style="left:480px; top:284px; width:100px;">
    <div class="big" style="font-size:25px; line-height:1;">Winner</div>
    <div style="font-size:22px; line-height:1.1;">of 8<br>Franchise<br>Awards</div>
  </div>

  <div class="fact" style="left:438px; top:388px; width:120px;">
    <div class="big" style="font-size:36px; line-height:1;">11</div>
    <div class="label">Team Members</div>
  </div>

  <div class="fact" style="left:234px; top:622px; width:110px; text-align:left;">
    <div class="big" style="font-size:40px; line-height:1;">123</div>
  </div>
  <div class="fact label" style="left:204px; top:659px; width:110px; font-size:15px;">combined</div>
  <div class="fact label" style="left:196px; top:678px; width:140px; font-size:15px; white-space:nowrap;">years of experience</div>

  <div class="brand" style="left:308px; top:714px; font-size:13px; width:86px; text-align:center;">Heritage<br>Rug Wash Co.</div>

  <div class="fact label" style="left:172px; top:736px; width:140px; font-size:15px;">Supporters of our<br>Local Health System</div>

  <div class="fact label" style="left:407px; top:682px; width:185px; text-align:left; font-size:17px; line-height:1.25;">Supporters of the "Kids"<br>programs<br>at the<br>QBFL</div>

  <!-- numeral five content -->
  <div class="fact" style="left:808px; top:160px; width:230px;">
    <div class="big" style="font-size:38px; line-height:1;">Winner</div>
    <div style="font-size:17px;">Falcon Outreach's<br>"Lift your Game " Award</div>
  </div>

  <div class="fact" style="left:692px; top:262px; width:120px;">
    <div class="big" style="font-size:40px; line-height:1;">60%</div>
    <div style="font-size:19px; line-height:1.4;">have been<br>with us</div>
    <div class="big" style="font-size:23px;">5+ years</div>
  </div>

  <div class="fact label" style="left:696px; top:416px; width:110px;">Making<br>Custom Rugs</div>
  <div class="fact label" style="left:690px; top:462px; width:100px;">Rug Binding</div>
  <div class="fact label" style="left:885px; top:386px; width:125px;">Carpet Cleaning</div>
  <div class="fact label" style="left:928px; top:425px; width:105px;">Oriental Rug<br>Cleaning</div>

  <div class="fact" style="left:950px; top:472px; width:135px;">
    <div class="big" style="font-size:30px; line-height:1;">Winner</div>
    <div style="font-size:17px; line-height:1.3;">Chamber of<br>Commerce<br>"Excellence in<br>Business"</div>
  </div>

  <div class="brand" style="left:680px; top:612px; font-size:15px; width:100px; text-align:center;">Loomhouse<br>Rug Studio</div>

  <div class="fact label" style="left:700px; top:666px; width:110px; font-size:15px; line-height:1.25;">Service Entire<br>Niagara<br>Region</div>

  <div class="fact" style="left:780px; top:696px; width:230px;">
    <div class="big" style="font-size:25px; line-height:1;">Gwendolyn and Ray</div>
    <div style="font-size:14px; line-height:1.3; margin-top:4px;">featured in magazine article<br>"Partners in Commerce"</div>
  </div>
</div>
</body>
</html>
```